Vel Oska Concrete Post Card Design Project

Hello, We are A Concrete Contractor. We specialize in removing and replacing concrete walkways, Patio's, Driveway's, ect., that are a trip hazard. We work a lot in Apartment complexes and Business Complexes where the trees have grown big and the roots from the trees lift up the concrete.
I would like someone to design a postcard (Two Sided) so I can send it out and market potential property manager customers. I would like to use our company logo on this card. Please see the pixel vault link below. Here are some things I would like the card to have on it.

1.Removal and Replacement of Concrete Sidewalks, Driveways, Parking Lots, Curb and Gutter.

2. ADA Compliant.

3. Repair of concrete tripping hazards and
root-damaged sidewalks.

4. Vel Oska Concrete brings your sidewalks in compliance with the Americans With Disabilities Act (ADA).

5. Property Management:

We cater to the needs of Property Mangement Companies, HOA, Apartment Complexes, Business Parks, Senior Living Complexes, Government Buildings and Shopping Centers.

6. Free Estimates
7. Contractors license number under our logo. It is:
BPLN #718390
8. Our phone numbers:555-284-9163 and 555-672-0394.

Card should be two sided 9" by 6"

Thank You
Updates

This website would not let me upload my logo so please click on the link below to get it.

 

http://i4471.pixelvault-host.com/albums/k218/Tvoska42/VelOskaConcreteLogo-2012-PROOF-2.jpg

Thank You

Reason: Hello, I have a lot of great designs. I have had a busy week and I am just now sitting down to ask for the changes I would like. Once I recieve all of the designs back with the changes I requested I would like to get the opinions of my coworkers and friends before selecting the design. I am asking for the deadline to be extended by 4 days. Thank You so much, Brenda Vel Oska

Target Market(s)

Property Managers

Industry/Entity Type

Concrete

Requirements
Must have
• Our logo

```html
<!DOCTYPE html>
<html lang="en">
<head>
<meta charset="utf-8">
<title>Vel Oska Concrete – Postcard</title>
<link href="https://fonts.googleapis.com/css2?family=Oswald:wght@600;700&display=swap" rel="stylesheet">
<style>
  :root {
    --backdrop: #fde21c;
    --concrete-light: #6a6a6a;
    --concrete-mid: #565656;
    --concrete-dark: #454545;
    --ink: #111111;
    --rule: #141414;
  }
  * { margin: 0; padding: 0; box-sizing: border-box; }
  html, body { width: 797px; height: 1200px; overflow: hidden; }
  body {
    background: var(--backdrop);
    font-family: "Oswald", "Arial Narrow", sans-serif;
    font-weight: 600;
    color: var(--ink);
    position: relative;
  }
  .card {
    position: absolute;
    left: 12px;
    width: 772px;
    height: 521px;
    overflow: hidden;
    box-shadow: 0 14px 12px -8px rgba(0,0,0,0.45);
  }
  .card--front { top: 24px; }
  .card--back  { top: 621px; }
  .concrete-surface {
    position: absolute; inset: 0;
    background:
      radial-gradient(ellipse 40% 30% at 30% 40%, var(--concrete-dark), transparent 70%),
      radial-gradient(ellipse 35% 25% at 75% 70%, var(--concrete-light), transparent 70%),
      radial-gradient(ellipse 30% 30% at 60% 20%, var(--concrete-light), transparent 70%),
      var(--concrete-mid);
  }
  .services {
    position: absolute; top: 42px; left: 0; right: 0;
    text-align: center;
    font-size: 11px;
    line-height: 14px;
    text-transform: uppercase;
  }
  .services p { margin-bottom: 26px; }
  .services .contact { font-size: 13px; margin-top: 4px; }
  .brand {
    position: absolute;
    text-align: center;
    line-height: 1;
    text-transform: uppercase;
    font-weight: 700;
  }
  .brand__name { display: block; font-size: 36px; }
  .brand__sub { display: block; font-size: 20px; margin-top: 4px; }
  .brand__license { display: block; font-size: 11px; margin-top: 5px; font-weight: 600; }
  .card--front .brand { left: 585px; top: 385px; width: 170px; }
  .audience {
    position: absolute;
    left: 42px; top: 36px;
    height: 445px;
    writing-mode: vertical-rl;
    font-size: 11.5px;
    line-height: 15px;
    text-transform: uppercase;
  }
  .card--back .brand {
    left: 150px; top: 176px;
    writing-mode: vertical-rl;
  }
  .card--back .brand__sub { margin-top: 0; margin-right: 6px; }
  .card--back .brand__license { margin-top: 0; margin-right: 6px; }
  .stamp-box {
    position: absolute;
    left: 612px; top: 42px;
    width: 87px; height: 111px;
    border: 1px solid var(--rule);
  }
  .address-lines {
    position: absolute;
    left: 408px; top: 303px;
    width: 291px;
  }
  .address-lines span {
    display: block;
    height: 38.5px;
    border-top: 1px solid var(--rule);
  }
</style>
</head>
<body>
  <section class="card card--front">
    <div class="concrete-surface" role="img" aria-label="Dark grey concrete texture background"></div>
    <div class="services">
      <p>Removal and replacement of concrete sidewalks, driveways, parkinglots, curb and gutters and ADA compliant.</p>
      <p>Concrete grinding: repair of tripping hazard removal, root-damaged sidewalks, 24 hr service.</p>
      <p>Vel Oska Concrete brings your sidewalks in compliance with the Americans with Disabilities Act (ADA).</p>
      <p class="contact">Free estimates &nbsp;·&nbsp; 555-284-9163 &nbsp;·&nbsp; 555-672-0394</p>
    </div>
    <div class="brand">
      <span class="brand__name">Vel Oska</span>
      <span class="brand__sub">Concrete</span>
      <span class="brand__license">BPLN #718390</span>
    </div>
  </section>

  <section class="card card--back">
    <div class="concrete-surface" role="img" aria-label="Dark grey concrete texture background"></div>
    <p class="audience">Property management: We cater to the needs of property management companies, HOA, apartment complexes, business parks, senior living complex, government buildings and shopping centers. Concrete trip hazard repair and removal. Sidewalk concrete repair.</p>
    <div class="brand">
      <span class="brand__name">Vel Oska</span>
      <span class="brand__sub">Concrete</span>
      <span class="brand__license">BPLN #718390 · 555-284-9163</span>
    </div>
    <div class="stamp-box"></div>
    <div class="address-lines">
      <span></span><span></span><span></span><span></span>
    </div>
  </section>
</body>
</html>
```